Natural Skincare brand needs new labels!

We are a natural and organic skin care brand based in the united states. We are looking for unique product label designs that will help our brand stand out. We want the labels to look elegant and natural, but also incorporate some color. We want a design aspect like a line drawing on the labels, see examples. Please refer to our website to see our current labels and to get more of a feel of who we are. Our logo is included. We are looking for 5 labels for 5 different Products.
1. Body butter: 1.5"x9" rectangle wrap around 12oz jar with black lid
2. Eczema Salve: 1.5" circle silver metal tin
3. Glow Serum: 1.5"x3" rectangle Blue Dropper Bottle with black top
4. Mineral Mist: 1.5"x3" clear glass sprayer bottle (want clear label)
website: www.velmirabotanics.com
Instagram: @velmirabotanics

```html
<!DOCTYPE html>
<html lang="en">
<head>
<meta charset="utf-8">
<title>Velmira — Glow Serum &amp; Mineral Mist Labels</title>
<link rel="stylesheet" href="https://fonts.googleapis.com/css2?family=Montserrat:wght@500;600&family=Open+Sans:wght@400;500&family=Roboto+Condensed:wght@300&family=Cormorant+Garamond:wght@500&display=swap">
<style>
  :root {
    --canvas: #ffffff;
    --label-tint: #e5ddd6;
    --ink: #2e2e2e;
    --ink-soft: #3a3a3a;
    --blush: #ef8a7a;
    --illustration: #cfc7c1;
  }
  * { margin: 0; padding: 0; box-sizing: border-box; }
  html, body { width: 1200px; height: 789px; overflow: hidden; background: var(--canvas); }
  .sheet { position: relative; width: 1200px; height: 789px; }

  .label-band {
    position: absolute; left: 43px; top: 325px;
    width: 518px; height: 268px;
    background: var(--label-tint);
  }

  .label {
    position: absolute; top: 320px; width: 260px; height: 280px;
    color: var(--ink);
  }
  .label--serum { left: 174px; }
  .label--mist { left: 736px; }

  .floral-drawing {
    position: absolute; left: 100px; top: 4px; width: 64px; height: 106px;
    border-radius: 30px 30px 8px 8px;
    background: radial-gradient(circle at 50% 45%, var(--illustration), transparent 75%);
    opacity: .85;
  }

  .brand {
    position: absolute; left: 0; top: 124px; width: 100%;
    display: flex; justify-content: center; align-items: center; gap: 6px;
    font-family: "Montserrat", sans-serif; font-weight: 500;
    font-size: 26px; letter-spacing: 1px; color: var(--blush);
  }
  .brand-dot {
    width: 10px; height: 10px; border-radius: 50%; background: var(--blush);
  }

  .product-name {
    position: absolute; left: 0; top: 177px; width: 100%;
    text-align: center;
    font-family: "Montserrat", sans-serif; font-weight: 500;
    font-size: 19px; letter-spacing: 5px; color: var(--ink-soft);
  }
  .product-rule {
    position: absolute; left: 46px; top: 205px; width: 168px; height: 1px;
    background: var(--ink-soft);
  }
  .product-tagline {
    position: absolute; left: 0; top: 212px; width: 100%;
    text-align: center;
    font-family: "Montserrat", sans-serif; font-weight: 600;
    font-size: 11px; line-height: 18px; letter-spacing: 2.4px; color: var(--ink);
  }
  .net-weight {
    position: absolute; left: 0; top: 250px; width: 100%;
    text-align: center;
    font-family: "Cormorant Garamond", serif; font-weight: 500;
    font-size: 9.5px; letter-spacing: 1.2px; color: var(--ink);
  }

  .ingredients {
    position: absolute; left: 272px; top: 251px; width: 230px;
    transform: rotate(-90deg); transform-origin: top left;
    font-family: "Open Sans", sans-serif; font-size: 10.2px; line-height: 14.6px;
    color: var(--ink);
  }

  .spec {
    position: absolute; left: 700px; width: 400px; text-align: center; color: #111;
  }
  .spec-size {
    top: 118px;
    font-family: "Roboto Condensed", sans-serif; font-weight: 300; font-size: 44px;
  }
  .spec-name {
    top: 181px;
    font-family: "Open Sans", sans-serif; font-weight: 500; font-size: 32px;
  }
</style>
</head>
<body>
<main class="sheet">
  <div class="label-band"></div>

  <section class="label label--serum">
    <div class="floral-drawing" role="img" aria-label="Fine line drawing of a blossoming flower branch"></div>
    <div class="brand"><span class="brand-dot"></span>Velmira</div>
    <h1 class="product-name">GLOW SERUM</h1>
    <div class="product-rule"></div>
    <p class="product-tagline">MANJITHA +SUNFLOWER<br>GLOW + EVEN SKIN TONE</p>
    <p class="net-weight">1 oz|29g</p>
    <p class="ingredients">Ingredients:<br>safflower oil^, sesame oil^, manjistha<br>powder^, rose petals^, turmeric^, carrot<br>seed oil^, sandalwood essential oil, ylang<br>ylang essential oil</p>
  </section>

  <p class="spec spec-size">1.5” X 3”</p>
  <p class="spec spec-name">Mineral Mist</p>

  <section class="label label--mist">
    <div class="floral-drawing" role="img" aria-label="Fine line drawing of a blossoming flower branch"></div>
    <div class="brand"><span class="brand-dot"></span>Velmira</div>
    <h2 class="product-name">GLOW SERUM</h2>
    <div class="product-rule"></div>
    <p class="product-tagline">MANJITHA +SUNFLOWER<br>GLOW + EVEN SKIN TONE</p>
    <p class="net-weight">1 oz|29g</p>
    <p class="ingredients">Ingredients:<br>safflower oil^, sesame oil^, manjistha<br>powder^, rose petals^, turmeric^, carrot<br>seed oil^, sandalwood essential oil, ylang<br>ylang essential oil</p>
  </section>
</main>
</body>
</html>
```